I need a book cover for my book titled Sunny Porch! The subtitle is Our Garden Years and the the author is Denisha Caldwell. I want the attached photo included on the cover, plus the words "I never met a chicken wing I didn't like!" The book size is 5.06 x 7.81 in. and is 146 pages. For the color scheme, I like a chocolate brown cover with aqua blue letters. (Please note that you don't have to use these colors. Feel free to use this color scheme or whatever you colors you like!)

• Please include my photo for the back cover, along with this text:

Sunny Porch! I was tired of being tired! I was tired of acid reflux, body stiffness, and being overweight. To make matters worse, I suffered from back pain, constipation, leg pain, and lack of sleep. If you are tired of looking to medical test for your answers, this is the book for you. The key was the day I decided to make “me” a priority by being #1 on my “to-do” list.

Our healthcare system seems to be more concerned about treating illness than they are about preventing it; which is why we have so many problems with our health and wellness. That’s why I’m going to give you insights into nutrition, health care, and the pharmaceutical industry.

I’m also going to give you some insights into exercise, supplements, detoxing and essential oils; as well as what goes into your grocery cart and the foods you feed your family.

Because you’re reading this I know you’re ready to live your best life, Sunny Porch! is for you.

Here’s to a healthy you!

Here's a brief bio about the author for the back cover:

Denisha lives in Chicago with her husband, Dr. Marvin, and has three adult children. She is probably one of the most private people you will meet – BUT HAD to tell her story!

```html
<!DOCTYPE html>
<html lang="en">
<head>
<meta charset="UTF-8">
<title>Sunny Porch! – Book Cover</title>
<link href="https://fonts.googleapis.com/css2?family=Delius&family=Arimo:wght@400;700&display=swap" rel="stylesheet">
<style>
  :root {
    --bg-teal: #3aa9a6;
    --aqua: #3cc6c4;
    --choc-dark: #2a1a10;
    --choc: #5a2c1e;
    --choc-mid: #6e3f2e;
    --choc-light: #8e6a5c;
    --warm-red: #a8282a;
    --warm-orange: #d9693a;
    --gold: #e3a12c;
    --white: #ffffff;
    --author: #5a2c1e;
  }
  * { margin: 0; padding: 0; box-sizing: border-box; }
  html, body { width: 1200px; height: 968px; overflow: hidden; }
  body {
    background: var(--bg-teal);
    position: relative;
    font-family: "Arimo", Arial, sans-serif;
  }
  .cover {
    position: absolute;
    top: 104px;
    width: 492px;
    height: 760px;
    overflow: hidden;
  }
  /* Back cover */
  .back-cover {
    left: 88px;
    background: linear-gradient(180deg, var(--choc-light) 0%, var(--choc) 20%, var(--choc) 100%);
  }
  .author-photo {
    position: absolute;
    left: 0; top: 150px;
    width: 100%; height: 290px;
    background: radial-gradient(ellipse at 45% 45%, #b07a50 0%, #7a4e32 45%, #3a2618 100%);
  }
  .bio-box {
    position: absolute;
    left: 0; top: 440px;
    width: 100%; height: 220px;
    background: var(--choc-dark);
    padding: 48px 70px 0 70px;
  }
  .bio-text {
    color: var(--aqua);
    font-size: 19px;
    line-height: 1.38;
    font-family: "Arimo", Arial, sans-serif;
  }
  /* Front cover */
  .front-cover {
    left: 620px;
    background:
      radial-gradient(ellipse 40% 18% at 25% 14%, rgba(190,180,70,0.55), transparent 70%),
      radial-gradient(ellipse 70% 30% at 55% 50%, rgba(217,105,58,0.85), transparent 75%),
      radial-gradient(ellipse 60% 25% at 70% 66%, rgba(168,40,42,0.9), transparent 75%),
      linear-gradient(180deg, var(--choc-mid) 0%, #8a5a48 20%, var(--choc) 80%, var(--choc) 100%);
  }
  .title {
    position: absolute;
    left: 0; right: 0; top: 58px;
    text-align: center;
    font-family: "Delius", "Comic Sans MS", cursive;
    color: var(--aqua);
    font-size: 128px;
    line-height: 0.92;
    text-shadow: 0 2px 6px rgba(0,0,0,0.25);
  }
  .title .line { display: block; }
  .subtitle {
    position: absolute;
    left: 0; right: 0; top: 332px;
    text-align: center;
    color: var(--white);
    font-weight: 700;
    font-size: 30px;
    text-shadow: 0 2px 4px rgba(0,0,0,0.35);
  }
  .author {
    position: absolute;
    left: 0; right: 0; top: 388px;
    text-align: center;
    color: var(--author);
    font-weight: 700;
    font-size: 17px;
  }
  .food-photo {
    position: absolute;
    left: 20px; top: 430px;
    width: 440px; height: 230px;
    border-radius: 14px;
    background: linear-gradient(135deg, #e9efe6 0%, #c9d7a0 18%, #d96a3a 45%, #a33a22 70%, #eeeeee 100%);
  }
  .tagline {
    position: absolute;
    right: 34px; top: 672px;
    width: 250px;
    color: var(--gold);
    font-weight: 700;
    font-size: 24px;
    line-height: 1.05;
  }
</style>
</head>
<body>
  <section class="cover back-cover">
    <div class="author-photo" role="img" aria-label="Portrait photo of the author smiling"></div>
    <div class="bio-box">
      <p class="bio-text">Denisha lives in Chicago with her husband, Dr. Marvin, and has three adult children. She is probably one of the most private people you will meet – BUT HAD to tell her story!</p>
    </div>
  </section>

  <section class="cover front-cover">
    <h1 class="title"><span class="line">Sunny</span><span class="line">Porch!</span></h1>
    <p class="subtitle">Our Garden Years</p>
    <p class="author">Denisha Caldwell.</p>
    <div class="food-photo" role="img" aria-label="Photo of glazed chicken wings on a white warning-label tray with celery, carrots and dip"></div>
    <p class="tagline">I never met a chicken wing I didn't like!</p>
  </section>
</body>
</html>
```